A hand soap seller needs a premium label for a new product

We need a premium label for a bottle of soap. We want to write on it:
VANTROSELLA (Name)
Hypoallergenic and antibacterial hand soap
350 ml e / 11.8 fl oz (volume, http://pimaxo.ru/7K3RtWbqmeL519)
Saint Petersburg - Russia / www.vantrosella.ru
We want to see the face of a hippopotamus in the design. Use only black and white and green for accents (the color of grass). Examples of a hippopotamus are shown in the photo. Our soap is hypoallergenic. Ideal for both children and adults. Therefore, the label should appeal to adults and children.
The bottle will be white, and the soap dispenser will be black.
So I'm attaching an example of a soap design that we liked
Label size: height-78 mm, width-102 mm !!!

Target Market(s)

Mothers and children

Industry/Entity Type

Hand soap

Font styles to use
Serif

Colors

Designer to choose only greyscale colors for use in the design.

Requirements
Must have
• The face of a hippopotamus emerging from the grass, Black and white palette with elements of green (grass color)
Nice to have
• The face of a hippopotamus emerging from the grass
Should not have
• Different colors

```html
<!DOCTYPE html>
<html lang="en">
<head>
<meta charset="utf-8">
<title>Velmora Hand Soap Label</title>
<link href="https://fonts.googleapis.com/css2?family=Jura:wght@300;400;500&display=swap" rel="stylesheet">
<style>
  :root {
    --teal: #17666e;
    --teal-bright: #14878a;
    --teal-deep: #115a66;
    --ink: #3a3b3d;
    --paper: #f4f6f8;
    --mist: #d9dee3;
    --swoosh-grey: #a9b0b6;
    --mascot-tone: #7d8794;
  }
  * { margin: 0; padding: 0; box-sizing: border-box; }
  html, body {
    width: 1200px; height: 918px; overflow: hidden;
    background: var(--paper);
  }
  .label {
    position: relative;
    width: 1200px; height: 918px;
    overflow: hidden;
    background: radial-gradient(ellipse at 68% 62%, #ffffff 0%, #f3f5f7 40%, #dde2e6 100%);
    font-family: "Jura", sans-serif;
  }
  .label__waves {
    position: absolute; inset: 0;
    width: 1200px; height: 918px;
  }
  .label__brand {
    position: absolute; left: 143px; top: 62px;
    font-size: 104px; font-weight: 400; line-height: 1;
    color: var(--teal); letter-spacing: 1px;
  }
  .label__brand-rule {
    position: absolute; left: 147px; top: 197px;
    width: 364px; height: 3px; background: var(--teal);
  }
  .label__descriptor {
    position: absolute; left: 143px; top: 222px;
    font-size: 64px; font-weight: 400; line-height: 1;
    color: var(--ink);
  }
  .label__product {
    position: absolute; left: 139px; top: 290px;
    font-size: 138px; font-weight: 400; line-height: 1;
    color: var(--teal);
  }
  .label__mascot {
    position: absolute; left: 47px; top: 465px;
    width: 458px; height: 432px;
    border-radius: 46% 46% 40% 40%;
    background: radial-gradient(ellipse at 45% 45%, var(--mascot-tone) 0%, #9aa3ad 55%, rgba(200,206,212,0.4) 85%, rgba(255,255,255,0) 100%);
  }
  .label__volume {
    position: absolute; right: 65px; top: 693px;
    font-size: 48px; font-weight: 400; line-height: 1;
    color: var(--ink); text-align: right;
  }
  .label__volume-rule {
    position: absolute; left: 729px; top: 757px;
    width: 406px; height: 3px; background: var(--teal);
  }
  .label__origin, .label__web {
    position: absolute; right: 65px;
    font-size: 31px; font-weight: 400; line-height: 1;
    color: var(--ink); text-align: right;
  }
  .label__origin { top: 774px; }
  .label__web { top: 816px; }
</style>
</head>
<body>
<main class="label">
  <svg class="label__waves" viewBox="0 0 1140 870" preserveAspectRatio="none" aria-hidden="true">
    <defs>
      <linearGradient id="tealBand" x1="0" y1="1" x2="1" y2="0">
        <stop offset="0" stop-color="#115a66"/>
        <stop offset="0.6" stop-color="#14878a"/>
        <stop offset="1" stop-color="#0f6d72"/>
      </linearGradient>
    </defs>
    <path d="M300,0 C600,120 900,400 1140,420 L1140,480 C880,470 620,180 250,0 Z" fill="#ffffff" opacity="0.45"/>
    <path d="M0,200 C300,150 700,300 1000,870 L940,870 C680,360 300,210 0,240 Z" fill="#ffffff" opacity="0.35"/>
    <path d="M0,700 C220,748 520,728 700,640 C520,752 250,770 0,748 Z" fill="#a9b0b6" opacity="0.8"/>
    <path d="M0,838 C400,770 780,560 1140,175 L1140,262 C900,500 620,720 0,842 Z" fill="url(#tealBand)"/>
    <path d="M470,740 C710,620 900,420 1015,219 C940,390 760,570 510,728 Z" fill="#115a66"/>
  </svg>

  <div class="label__brand">velmora</div>
  <div class="label__brand-rule"></div>
  <div class="label__descriptor">hypoallergenic</div>
  <div class="label__product">Hand Soap</div>

  <div class="label__mascot" role="img" aria-label="Cartoon hippopotamus mascot sitting"></div>

  <div class="label__volume">350 ml e / 11,8 fl.oz.</div>
  <div class="label__volume-rule"></div>
  <div class="label__origin">saints-petersburg - russia</div>
  <div class="label__web">www.velmorasoap.ru</div>
</main>
</body>
</html>
```